Business Cards for Retail/Sourcing Business.

We need a business cards for our company where it looks like:
TK
LM

VERTICAL, where the TK is over the LM. Then Under the TKLM would be name, address and website address. We want the P to be in the style of our original logo, which I uploaded.

Also, can we get a couple of designs with fun colors - especially for the letter head.

Target Market(s)

Old clients. Many of our clients or people we do business with are 40-50 plus. We are not an industry with many young people.

Industry/Entity Type

Business

Contact Information for Business Card

Front side is just says TKLM with name, title, address, and website below.

Font styles to use
Serif
Sans Serif
Decorative
Script

Requirements
Must have
• THE TKLM design with the P in the design of the logo
Nice to have
• Fun colors, new takes on the TKLM and any other additions that would be cool and make it pop

```html
<!DOCTYPE html>
<html lang="en">
<head>
<meta charset="utf-8">
<title>TKLM Stationery</title>
<link href="https://fonts.googleapis.com/css2?family=Saira:wght@400;500;600&display=swap" rel="stylesheet">
<style>
  :root {
    --backdrop: #cfcfcf;
    --ink-dark: #0d0f14;
    --ink-panel: #161a22;
    --brand-blue: #2b3f9e;
    --name-blue: #3d4f9f;
    --paper: #ffffff;
    --watermark: #e6e6e6;
    --silver: #c9ccd2;
    --text-light: #f2f2f2;
    --text-dark: #111111;
  }
  * { margin: 0; padding: 0; box-sizing: border-box; }
  html, body { width: 1200px; height: 900px; overflow: hidden; }
  body {
    background: var(--backdrop);
    font-family: "Saira", sans-serif;
    position: relative;
  }

  .wordmark {
    font-family: "Saira", sans-serif;
    font-weight: 600;
    color: var(--brand-blue);
    line-height: 0.92;
    letter-spacing: 2px;
  }

  /* Business cards */
  .card {
    position: absolute;
    width: 239px;
    height: 406px;
    overflow: hidden;
  }
  .card--dark { left: 44px; top: 410px; background: var(--ink-dark); }
  .card--light { left: 916px; top: 406px; background: var(--paper); }

  .card__brand {
    height: 218px;
    display: flex;
    align-items: center;
    justify-content: center;
    text-align: center;
  }
  .card__brand .wordmark { font-size: 82px; }
  .card--dark .card__brand { background: linear-gradient(#15181f, #0a0c10); }
  .card--dark .card__brand .wordmark { color: #4a5fc4; }
  .card--light .card__brand { height: 214px; }

  .card__rule { height: 6px; }
  .card--dark .card__rule { background: linear-gradient(90deg, #555, var(--silver), #555); }
  .card--light .card__rule { height: 8px; background: var(--brand-blue); }

  .card__details {
    background: linear-gradient(#1a1e26, var(--ink-dark));
    height: 182px;
    color: var(--text-light);
    text-align: center;
    padding-top: 16px;
  }
  .card__name { font-size: 21px; color: var(--name-blue); letter-spacing: 0.5px; line-height: 1.1; }
  .card__title { font-size: 15px; line-height: 1.2; margin-bottom: 16px; }
  .card__phone { font-size: 20px; font-weight: 500; line-height: 1.1; letter-spacing: 0.5px; }
  .card__line { font-size: 15px; line-height: 1.3; letter-spacing: 0.4px; }

  /* Letterhead */
  .letterhead {
    position: absolute;
    left: 317px;
    top: 95px;
    width: 559px;
    height: 722px;
    background: var(--paper);
    overflow: hidden;
  }
  .letterhead__brand { position: absolute; left: 14px; top: 14px; }
  .letterhead__brand .wordmark { font-size: 84px; }
  .letterhead__watermark {
    position: absolute;
    left: 150px;
    top: 300px;
    font-size: 210px;
    color: var(--watermark);
    line-height: 0.9;
  }
  .letterhead__contact {
    position: absolute;
    left: 20px;
    right: 24px;
    top: 664px;
    display: flex;
    justify-content: space-between;
    font-size: 13px;
    font-weight: 500;
    color: var(--text-dark);
    letter-spacing: 0.3px;
  }
  .letterhead__rule {
    position: absolute; left: 0; right: 0; top: 687px; height: 5px;
    background: linear-gradient(90deg, #1c2a6e, var(--brand-blue), #1c2a6e);
  }
  .letterhead__footer {
    position: absolute; left: 0; right: 0; top: 692px; height: 30px;
    background: var(--ink-panel);
  }
</style>
</head>
<body>

  <section class="card card--dark" aria-label="Business card, dark edition">
    <div class="card__brand"><div class="wordmark">TK<br>LM</div></div>
    <div class="card__rule"></div>
    <div class="card__details">
      <p class="card__name">Marla Quent</p>
      <p class="card__title">home Sourcing</p>
      <p class="card__phone">0401287466</p>
      <p class="card__line">41 east 9th street</p>
      <p class="card__line">LM,LM</p>
      <p class="card__line">www.tklmsource.com</p>
    </div>
  </section>

  <section class="letterhead" aria-label="Letterhead">
    <div class="letterhead__watermark wordmark" aria-hidden="true">TK<br>LM</div>
    <div class="letterhead__brand"><div class="wordmark">TK<br>LM</div></div>
    <div class="letterhead__contact">
      <span>0401287466</span>
      <span>41 east 9th street LM,LM</span>
      <span>www.tklmsource.com</span>
    </div>
    <div class="letterhead__rule"></div>
    <div class="letterhead__footer"></div>
  </section>

  <section class="card card--light" aria-label="Business card, light edition">
    <div class="card__brand"><div class="wordmark">TK<br>LM</div></div>
    <div class="card__rule"></div>
    <div class="card__details">
      <p class="card__name">Marla Quent</p>
      <p class="card__title">home Sourcing</p>
      <p class="card__phone">0401287466</p>
      <p class="card__line">41 east 9th street</p>
      <p class="card__line">LM,LM</p>
      <p class="card__line">www.tklmsource.com</p>
    </div>
  </section>

</body>
</html>
```